Ember & Gloss Detail Co. new business cards

I am a business owner who professionally details cars. I clean and detail the interiors, exteriors of vehicles. I need a logo designed for my new business Ember & Gloss Detail Co. and a great designed card that will wow anyone that I hand it out to. Attached is a photo that I would like on side of the card. I want the picture to be on the right side of the card, while my busines name will be on the other side. I want the picture to have a slant where it divided the card into left and right, not just straight down. The picture will be printed glossy and I want the left half to have a carbon fiber background. Feel free to design a cool font for the business name, The business name needs to be a red gloss to pop out against the matte background. The back of the card should have my name Colin Marchetti. Under my name should be Owner/ Operator. then all my contact info and fb and instagram stuff. must include services offered- Paint Correction, Exterior detailing
Interior Detailing, Engine Bay Detailing, Headlight restoration, Ceramic Coatings

Target Market(s)

My target market is anyone who drives a vehicle.

Industry/Entity Type

Automotive

Contact Information for Business Card

Business name- Ember & Gloss Detail Co.
Colin Marchetti Owner/ Operator
Location- Harlow Springs, OR
Business # (555) 214-6079
email- colin@thebrightpolisher.example
fb and instragram logos- @thebrightpolisher

Font styles to use
Serif
Script
Other font styles liked:
• Blacksword

Colors
ec1f27
000000

Requirements
Must have
• The card must be in landscape position. All the details that are in the brief description which are my business name, my name, services offered and any other info thats in the project description. I uploaded pics of veltranos that I would like to see different designs incorporated into the backside of the card. File 5,6,and 7 are ideas that I would like to see done with my business name. The diamond around my name with the polisher coming around the bottom, and a Veltrano outline on the left side of the diamond kinda like file 5
• Also, business name and name should be in some style of script, while the rest of the fonts in serif. Must have the picture of me on the front right side of the card!!!
Nice to have
• Your own personal ideas that you think I am missing.
Should not have
• No grafitti, no generic logos around the business name like every other auto detail card on google.

```html
<!DOCTYPE html>
<html lang="en">
<head>
<meta charset="utf-8">
<title>Ember &amp; Gloss Detail Co. — Business Card</title>
<link rel="stylesheet" href="https://fonts.googleapis.com/css2?family=Great+Vibes&family=Open+Sans:wght@400;600&display=swap">
<style>
  :root {
    --stage: #2a2a2a;
    --card: #050505;
    --card-glow: #161616;
    --red: #ec1f27;
    --red-deep: #b0121a;
    --text: #e6e6e6;
    --muted: #bdbdbd;
    --icon: #e6e6e6;
  }
  * { box-sizing: border-box; margin: 0; padding: 0; }
  html, body { width: 1200px; height: 800px; overflow: hidden; }
  body {
    background: var(--stage);
    font-family: "Open Sans", sans-serif;
    display: flex;
    flex-direction: column;
    align-items: center;
    justify-content: center;
    gap: 36px;
  }
  .card {
    position: relative;
    width: 630px;
    height: 360px;
    background: radial-gradient(ellipse at 60% 40%, var(--card-glow) 0%, var(--card) 70%);
    box-shadow: 0 10px 30px rgba(0,0,0,.6);
    overflow: hidden;
  }
  .card__frame {
    position: absolute;
    inset: 14px;
    border: 1.5px solid var(--red-deep);
    pointer-events: none;
  }
  .script { font-family: "Great Vibes", cursive; color: var(--red); font-weight: 400; line-height: 1; }

  /* Front */
  .front__brand {
    position: absolute;
    left: 62px;
    top: 145px;
    font-size: 38px;
  }
  .front__brand span { display: block; }
  .front__brand span + span { margin-left: 26px; margin-top: 6px; }
  .front__car {
    position: absolute;
    right: 40px;
    top: 60px;
    width: 270px;
    height: 200px;
    border-radius: 40% 40% 30% 30%;
    background:
      radial-gradient(ellipse at 50% 40%, rgba(236,31,39,.45) 0%, rgba(236,31,39,0) 35%),
      radial-gradient(ellipse at 50% 50%, #1e1e1e 0%, #0a0a0a 60%, rgba(5,5,5,0) 75%);
  }

  /* Back */
  .back__photo {
    position: absolute;
    right: 14px;
    top: 14px;
    width: 220px;
    height: 160px;
    background: radial-gradient(ellipse at 55% 45%, #3b5070 0%, #1d2a3e 40%, rgba(5,5,5,0) 75%);
  }
  .back__brand {
    position: absolute;
    left: 310px;
    top: 66px;
    font-size: 18px;
  }
  .back__brand span { display: block; }
  .back__brand span + span { margin-left: 10px; margin-top: 2px; }
  .back__name {
    position: absolute;
    left: 44px;
    top: 150px;
    font-size: 46px;
  }
  .back__role {
    position: absolute;
    left: 62px;
    top: 204px;
    font-size: 12px;
    color: var(--muted);
  }
  .contact {
    position: absolute;
    left: 44px;
    top: 232px;
    list-style: none;
    display: flex;
    flex-direction: column;
    gap: 4px;
  }
  .contact__item {
    display: flex;
    align-items: center;
    gap: 8px;
    font-size: 11.5px;
    line-height: 16px;
    color: var(--text);
  }
  .contact__icon { width: 14px; height: 14px; flex: none; }
  .services {
    position: absolute;
    right: 40px;
    top: 186px;
    list-style: none;
    font-size: 11px;
    line-height: 15px;
    color: var(--text);
  }
  .services li { margin-bottom: 3px; }
  .services li::before { content: "•"; color: var(--muted); margin-right: 8px; }
</style>
</head>
<body>

  <section class="card card--front" aria-label="Card front">
    <div class="card__frame"></div>
    <h1 class="front__brand script"><span>Ember &amp; Gloss</span><span>Detail Co.</span></h1>
    <div class="front__car" role="img" aria-label="Photo of a black sports car seen from the front with red accents"></div>
  </section>

  <section class="card card--back" aria-label="Card back">
    <div class="card__frame"></div>
    <div class="back__photo" role="img" aria-label="Photo of the owner polishing a car"></div>
    <p class="back__brand script"><span>Ember &amp; Gloss</span><span>Detail Co.</span></p>
    <h2 class="back__name script">Colin Marchetti</h2>
    <p class="back__role">Owner/ Operator</p>

    <ul class="contact">
      <li class="contact__item">
        <svg class="contact__icon" viewBox="0 0 16 16" aria-hidden="true"><circle cx="8" cy="8" r="8" fill="var(--icon)"/><path d="M5.2 4.2l1.6 1.6-.8 1.1c.6 1.2 1.5 2.1 2.7 2.7l1.1-.8 1.6 1.6-1 1.2C7.5 11.4 4.6 8.5 4 5.2z" fill="#000"/></svg>
        (555) 214-6079
      </li>
      <li class="contact__item">
        <svg class="contact__icon" viewBox="0 0 16 16" aria-hidden="true"><circle cx="8" cy="8" r="8" fill="var(--icon)"/><rect x="4" y="5" width="8" height="6" fill="none" stroke="#000"/><path d="M4 5l4 3.3L12 5" fill="none" stroke="#000"/></svg>
        colin@thebrightpolisher.example
      </li>
      <li class="contact__item">
        <svg class="contact__icon" viewBox="0 0 16 16" aria-hidden="true"><circle cx="8" cy="8" r="8" fill="var(--icon)"/><circle cx="8" cy="8" r="4" fill="none" stroke="#000"/><path d="M4 8h8M8 4c-1.6 2.4-1.6 5.6 0 8M8 4c1.6 2.4 1.6 5.6 0 8" fill="none" stroke="#000" stroke-width=".8"/></svg>
        www.thebrightpolisher.example
      </li>
      <li class="contact__item">
        <svg class="contact__icon" viewBox="0 0 16 16" aria-hidden="true"><circle cx="8" cy="8" r="8" fill="var(--icon)"/><path d="M8 3.5a3 3 0 0 0-3 3c0 2.2 3 5.8 3 5.8s3-3.6 3-5.8a3 3 0 0 0-3-3zm0 4.2a1.2 1.2 0 1 1 0-2.4 1.2 1.2 0 0 1 0 2.4z" fill="#000"/></svg>
        Harlow Springs, OR
      </li>
      <li class="contact__item">
        <svg class="contact__icon" viewBox="0 0 16 16" aria-hidden="true"><circle cx="8" cy="8" r="8" fill="var(--icon)"/></svg>
        @thebrightpolisher
      </li>
    </ul>

    <ul class="services" aria-label="Services">
      <li>Paint correction</li>
      <li>Exterior detailing</li>
      <li>Interior detailing</li>
      <li>Engine bay detailing</li>
      <li>Headlight restoration</li>
      <li>Ceramic coatings</li>
    </ul>
  </section>

</body>
</html>
```